Bayshore Pacers Dashday - 2 posters

We need two community event posters for an annual marathon with continuity in design showcasing the clubs logo colours and community spirit. Poster one is for the Juniors division which needs to look like a fun day encouraging families to come down and register and compete. It will be distributed to all the schools and social media. Poster two is for the main event again attracting registration with prizes. Encouraging all levels of runners from professionals to amateurs family friendly. It is in a unique location along the city's foreshore with amazing views.

Target Market(s)

Marathon runners, juniors, community and families

Requirements
Must have
• photos, logos details
Nice to have
• We are looking for a motivating high energy poster to entice registration and feel like fun event for the whole comminty

```html
<!DOCTYPE html>
<html lang="en">
<head>
<meta charset="utf-8">
<title>Bayshore Pacers Junior Dashday Poster</title>
<link href="https://fonts.googleapis.com/css2?family=Questrial&family=Poppins:wght@500;600&display=swap" rel="stylesheet">
<style>
:root{
  --navy:#2f4e74;
  --orange:#ee8233;
  --white:#ffffff;
  --ink:#1d1d1d;
  --stage:#f2f2f2;
}
html,body{margin:0;padding:0;width:1200px;height:1198px;overflow:hidden;background:var(--stage);}
.poster{
  position:absolute;left:209px;top:47px;width:946px;height:1336px;
  transform:scale(0.8276);transform-origin:0 0;
  background:var(--white);overflow:hidden;
  font-family:"Questrial",sans-serif;color:var(--white);
}
.artwork{position:absolute;left:0;top:0;width:946px;height:1085px;}
.brand{position:absolute;left:22px;top:532px;width:160px;text-align:center;color:var(--navy);font-family:"Questrial",sans-serif;}
.brand-mark{width:56px;height:56px;border-radius:50%;background:#27a6b8;margin:0 auto 8px;}
.brand-name{font-size:17px;line-height:1.15;}
.event-title{position:absolute;left:24px;top:708px;margin:0;font-weight:400;font-size:43px;line-height:53px;letter-spacing:2px;}
.rule{position:absolute;height:2px;background:linear-gradient(90deg,rgba(255,255,255,.9),rgba(255,255,255,.9) 70%,rgba(255,255,255,0));}
.rule-one{left:12px;top:834px;width:370px;}
.rule-two{left:12px;top:942px;width:470px;}
.venue{position:absolute;left:23px;top:848px;}
.venue-label{font-family:"Poppins",sans-serif;font-weight:600;font-size:31px;line-height:36px;letter-spacing:1px;}
.venue-place{font-size:28px;line-height:36px;}
.distances{position:absolute;left:23px;top:960px;margin:0;padding:0;list-style:none;font-size:28px;line-height:36px;}
.register{position:absolute;right:12px;top:1030px;text-align:right;}
.register-note{color:var(--ink);font-size:15px;}
.register-url{color:var(--navy);font-size:20px;}
.thanks{position:absolute;left:0;top:1085px;width:946px;height:102px;background:var(--navy);box-sizing:border-box;padding:9px 24px 0 25px;font-size:15.3px;line-height:24px;letter-spacing:-.2px;}
.partners{position:absolute;left:0;top:1187px;width:946px;height:101px;display:flex;align-items:center;justify-content:space-around;padding:0 24px;box-sizing:border-box;color:var(--navy);font-size:21px;}
.partner{display:flex;align-items:center;gap:8px;}
.partner-dot{width:26px;height:26px;border-radius:50%;background:var(--orange);}
.tagbar{position:absolute;left:0;top:1288px;width:946px;height:48px;background:var(--navy);display:flex;align-items:center;justify-content:space-between;padding:0 44px 0 47px;box-sizing:border-box;}
.hashtags{font-size:21px;letter-spacing:1px;}
.social{display:flex;gap:10px;}
.social span{width:22px;height:22px;border:2px solid var(--white);border-radius:4px;box-sizing:border-box;}
</style>
</head>
<body>
<main class="poster">
  <svg class="artwork" viewBox="0 0 946 1085" xmlns="http://www.w3.org/2000/svg">
    <defs>
      <linearGradient id="raceStart" x1="0" y1="0" x2="0" y2="1">
        <stop offset="0" stop-color="#9fc0d8"/>
        <stop offset=".35" stop-color="#c9d3da"/>
        <stop offset=".6" stop-color="#8a6f74"/>
        <stop offset="1" stop-color="#6d8a4e"/>
      </linearGradient>
      <linearGradient id="podium" x1="0" y1="0" x2="0" y2="1">
        <stop offset="0" stop-color="#b9cbe0"/>
        <stop offset=".55" stop-color="#d9d6d2"/>
        <stop offset="1" stop-color="#7f8f5a"/>
      </linearGradient>
    </defs>
    <polygon points="0,0 946,0 946,300 110,520 0,425" fill="url(#raceStart)" role="img" aria-label="Photo of young runners sprinting from the start line on the foreshore"/>
    <polygon points="374,757 946,585 946,1025 669,1025" fill="url(#podium)" role="img" aria-label="Photo of junior winners celebrating on the podium with the race announcer"/>
    <polygon points="0,690 300,690 735,1085 0,1085" fill="var(--orange)"/>
    <polygon points="110,520 946,258 946,585 374,757 300,690" fill="var(--navy)"/>
    <line x1="243" y1="640" x2="946" y2="416" stroke="var(--white)" stroke-width="3"/>
    <g fill="var(--white)" font-family="Questrial, sans-serif" text-anchor="middle" letter-spacing="3">
      <text x="544" y="452" font-size="50" transform="rotate(-17.4 544 435)">June 30, 2018</text>
      <text x="562" y="500" font-size="50" transform="rotate(-17.4 562 483)">4.00 pm onwards</text>
      <text x="612" y="595" font-size="48" letter-spacing="1" transform="rotate(-17.4 612 578)">Great Prizes &amp; Fun for the</text>
      <text x="627" y="650" font-size="48" letter-spacing="1" transform="rotate(-17.4 627 633)">whole family</text>
    </g>
  </svg>

  <div class="brand">
    <div class="brand-mark"></div>
    <div class="brand-name">Bayshore Pacers<br>Dashday</div>
  </div>

  <h1 class="event-title">2018 Pacers<br>Junior Dashday</h1>
  <div class="rule rule-one"></div>
  <div class="venue">
    <div class="venue-label">Start/Finish</div>
    <div class="venue-place">Foreshore-Bayshore Yacht Club</div>
  </div>
  <div class="rule rule-two"></div>
  <ul class="distances">
    <li>1 mile (1.6km) 3-6 years old</li>
    <li>2 miles (3.2km) 7-11 years old</li>
    <li>3 miles (4.8km) 12-16 years old</li>
  </ul>

  <div class="register">
    <div class="register-note">Don't miss out to Register at</div>
    <div class="register-url">bayshoredashday.com</div>
  </div>

  <p class="thanks" style="margin:0">Bayshore Pacers Club proudly presents this event to the Community with thanks to generous Sponsors, Partners and Volunteers including - Kestrel Electrical | The Runners Stride | Shoreline Fireworks | The Harbourview Apartment Hotel | Toastie Hut | Marlo Finch Jewelers | Core9 | Bayshore Motors | Dale Morrow MLA | CREMA | Hazel Trent Naturopathics | Topup Fuels | Pharmacy 212 | Sports Lane | The Heel &amp; Toe Bayshore | Porter &amp; Lane | CRU | Glenn Avery Homes | Brightside Print.</p>

  <div class="partners">
    <div class="partner"><span class="partner-dot"></span>Pacers</div>
    <div class="partner">Wellcove</div>
    <div class="partner">City of Bayshore</div>
    <div class="partner">Linkwave</div>
    <div class="partner">Lumen Events</div>
    <div class="partner">Holt's Grocers</div>
  </div>

  <div class="tagbar">
    <div class="hashtags">#pacersdashday #welovemarathons #fitnessforlife</div>
    <div class="social"><span></span><span></span><span></span></div>
  </div>
</main>
</body>
</html>
```